Exciting new Aussie social network app - designer wanted!

Interested in this entire Freelance Job?
Here is the full project link:
http://jobs.pixelquarry.com.au/job.aspx?id=582716
****
We are a startup based in Melbourne working on a hot new iOS/Android social media app with an edge.
We have completed the scoping phase with the app developers and we are currently seeking a talented app UI/UX designer to work with to create something highly polished.
Our aim with this competition is to mockup the first screen of our app and effectively meet the designer we would love to move forward with to complete the entire design phase after a full debrief. Our app will be comparable to the look/feel of the Quillmoss or Glimmerdot apps, however, the functionality will be a little different. One of our app's main features does involve sharing smartphone captured photos to a stream (stylised gallery of photos) on a network.
We are inspired by the design language of the following iOS apps:
Quillmoss
https://apps.velmora.example/au/app/quillmoss/id813560274?mt=8
Barvo
https://apps.velmora.example/au/app/barvo/id690134827?mt=8
Hoxwelt
https://apps.velmora.example/au/app/hoxwelt/id731842056?mt=8
Lumbrazet
https://apps.velmora.example/au/app/lumbrazet/id572019386?mt=8
Please refer to the screenshot attached entitled MAIN SCREEN and create your own version of this UI/UX for this competition.
Our requirements -
* The title at the top title bar is called "Zorvy"
* the 5 navigation text & buttons at the bottom dock from left to right are:
FEED (Icon of a map pin drop), PEOPLE (Icon of 3 people), CAMERA graphic or a PLUS (+) symbol or both without text label, ACTIVITY(chat boxes/hearts), ME (Icon of Person)
* We need to see what the dock items would like like in each of the 5 states. Eg. What would it look like then the FEED state is highlighted when the user is in the feed section of the app.
* Screen to display whether you are following these users or displaying content from all users.
* We want a small text overlay over each image in the corner, perhaps semi-transparent, to show a 3-4 character code and a heart symbol to like the image.
* We need to see at least 1 new notification any of the dock items
Please refer to attached files for further illustration of buttons we have considered.
Thank you very much for your effort!
We look forward to your mockup and hopefully further work together!
If you are interested in this entire job check out our link to the full freelance project:
Target Market(s)
18-35 years, we expect a more female user demographic, but want to appeal to both sexes.
Industry/Entity Type
Camera
Look and feel

```html
<!DOCTYPE html>
<html lang="en">
<head>
<meta charset="utf-8">
<title>Zorvy – Main Screen</title>
<link rel="stylesheet" href="https://fonts.googleapis.com/css2?family=Questrial&family=Arimo:wght@400;700&display=swap">
<style>
  :root {
    --page-bg: #efefef;
    --status-bg: #111111;
    --status-text: #ffffff;
    --header-bg: rgba(186, 203, 220, 0.88);
    --header-ink: #3f5d7e;
    --seg-fill: rgba(200, 210, 222, 0.75);
    --seg-line: rgba(210, 220, 232, 0.85);
    --seg-ink-on: #4c5f76;
    --seg-ink-off: #c8d3df;
    --label-ink: #eef2f2;
    --date-ink: #ffffff;
    --tag-bg: rgba(20, 28, 40, 0.45);
    --tag-ink: #ffffff;
    --dock-bg: rgba(190, 205, 170, 0.78);
    --dock-ink: #3c5a3a;
    --dock-active-ink: #d7dec8;
    --badge-bg: #e9264c;
    --badge-ink: #ffffff;
    --bg-top: #3d526e;
    --bg-mid: #4f5f6c;
    --bg-bottom: #4c6444;
  }
  * { box-sizing: border-box; margin: 0; padding: 0; }
  html, body { width: 1200px; height: 1200px; overflow: hidden; background: var(--page-bg); }
  body { position: relative; font-family: "Questrial", sans-serif; }

  .app-screen {
    position: absolute; left: 276px; top: 20px; width: 648px; height: 1160px; overflow: hidden;
    background:
      radial-gradient(ellipse 70% 40% at 0% 100%, rgba(150,130,50,0.75), rgba(150,130,50,0) 70%),
      linear-gradient(180deg, var(--bg-top) 0%, var(--bg-mid) 50%, #506a58 75%, var(--bg-bottom) 100%);
  }

  .status-bar {
    position: absolute; left: 0; top: 0; width: 100%; height: 50px; background: var(--status-bg);
    color: var(--status-text); font-family: "Arimo", sans-serif; font-weight: 700; font-size: 26px;
    display: flex; align-items: center;
  }
  .status-bar .carrier { position: absolute; left: 10px; display: flex; align-items: center; gap: 8px; }
  .status-bar .clock { position: absolute; left: 0; right: 0; text-align: center; }
  .status-bar .status-icons { position: absolute; right: 8px; display: flex; align-items: center; gap: 14px; }

  .title-bar { position: absolute; left: 0; top: 50px; width: 100%; height: 87px; background: var(--header-bg); }
  .title-bar .menu-button { position: absolute; left: 42px; top: 22px; }
  .title-bar .app-name {
    position: absolute; left: 0; right: 0; top: 18px; text-align: center; color: var(--header-ink);
    font-size: 44px; letter-spacing: 1px;
  }
  .title-bar .search-button { position: absolute; right: 24px; top: 16px; }

  .feed-toggle {
    position: absolute; left: 145px; top: 165px; width: 338px; height: 39px;
    border: 2px solid var(--seg-line); border-radius: 4px; display: flex; overflow: hidden; font-size: 21px;
  }
  .feed-toggle span { flex: 1; display: flex; align-items: center; justify-content: center; }
  .feed-toggle .is-selected { background: var(--seg-fill); color: var(--seg-ink-on); }
  .feed-toggle .is-idle { color: var(--seg-ink-off); }

  .photo-card { position: absolute; width: 200px; margin-left: -100px; text-align: center; }
  .photo-frame {
    position: relative; width: 102px; height: 102px; margin: 0 auto; border-radius: 22px; overflow: hidden;
  }
  .photo-frame.tone-blue { background: linear-gradient(160deg, #31c4fb, #1576ea); }
  .photo-frame.tone-green { background: linear-gradient(160deg, #1ef28a, #0fd9b9); }
  .photo-frame.tone-orange { background: linear-gradient(160deg, #ff7a3c, #fb6a58); }
  .photo-frame.tone-red { background: linear-gradient(160deg, #f3506a, #e9264c); }
  .photo-frame.tone-yellow { background: linear-gradient(160deg, #fff52e, #e8d51a); }
  .photo-tag {
    position: absolute; right: 6px; bottom: 6px; height: 20px; padding: 0 6px; border-radius: 10px;
    background: var(--tag-bg); color: var(--tag-ink); font-family: "Arimo", sans-serif; font-weight: 700;
    font-size: 11px; display: flex; align-items: center; gap: 4px;
  }
  .photo-card .photo-name { margin-top: 22px; color: var(--label-ink); font-size: 20px; white-space: nowrap; }
  .photo-card .photo-date {
    margin-top: 6px; color: var(--date-ink); font-family: "Arimo", sans-serif; font-weight: 700; font-size: 13px;
  }

  .dock { position: absolute; left: 0; bottom: 0; width: 100%; height: 98px; display: flex; }
  .dock-item {
    position: relative; flex: 0 0 129.6px; display: flex; align-items: center; justify-content: center;
    background: var(--dock-bg); color: var(--dock-ink);
  }
  .dock-item.is-active { background: transparent; color: var(--dock-active-ink); }
  .notice-badge {
    position: absolute; left: 78px; top: 6px; min-width: 24px; height: 24px; padding: 0 6px; border-radius: 12px;
    background: var(--badge-bg); color: var(--badge-ink); font-family: "Arimo", sans-serif; font-weight: 700;
    font-size: 14px; display: flex; align-items: center; justify-content: center;
  }
</style>
</head>
<body>
<svg width="0" height="0" style="position:absolute" aria-hidden="true">
  <defs>
    <symbol id="tag-heart" viewBox="0 0 20 18">
      <path d="M10 17 C4 12 1 9 1 5.5 a4.5 4.5 0 0 1 9 -1.5 a4.5 4.5 0 0 1 9 1.5 C19 9 16 12 10 17 z" fill="#ffffff"/>
    </symbol>
  </defs>
</svg>

<main class="app-screen">
  <header class="status-bar">
    <div class="carrier">
      <svg width="28" height="10" viewBox="0 0 28 10" aria-hidden="true"><rect x="0" y="4" width="3" height="6" fill="#fff"/><rect x="5" y="2" width="3" height="8" fill="#fff"/><rect x="10" y="8" width="3" height="2" fill="#fff"/><rect x="15" y="8" width="3" height="2" fill="#fff"/><rect x="20" y="8" width="3" height="2" fill="#fff"/></svg>
      <span>Korralink</span>
      <svg width="30" height="22" viewBox="0 0 30 22" aria-hidden="true"><path d="M2 8 a18 18 0 0 1 26 0" fill="none" stroke="#fff" stroke-width="3.5"/><path d="M7 13 a11 11 0 0 1 16 0" fill="none" stroke="#fff" stroke-width="3.5"/><path d="M11 18 l4 4 l4 -4 a6 6 0 0 0 -8 0 z" fill="#fff"/></svg>
    </div>
    <div class="clock">11:11 AM</div>
    <div class="status-icons">
      <svg width="32" height="30" viewBox="0 0 32 30" aria-hidden="true"><path d="M26 12 a11 11 0 1 0 -2 10" fill="none" stroke="#fff" stroke-width="3"/><path d="M22 10 l6 4 l1 -7 z" fill="#fff"/><rect x="9" y="13" width="10" height="8" fill="#fff"/><path d="M11 13 v-3 a3 3 0 0 1 6 0 v3" fill="none" stroke="#fff" stroke-width="2"/></svg>
      <svg width="22" height="22" viewBox="0 0 22 22" aria-hidden="true"><path d="M21 1 L1 10 L10 12 L12 21 z" fill="#fff"/></svg>
      <svg width="42" height="20" viewBox="0 0 42 20" aria-hidden="true"><rect x="1.5" y="1.5" width="35" height="17" rx="2" fill="none" stroke="#fff" stroke-width="2"/><rect x="4" y="4" width="30" height="12" fill="#fff"/><rect x="38" y="6" width="3" height="8" fill="#fff"/></svg>
    </div>
  </header>

  <nav class="title-bar">
    <svg class="menu-button" width="47" height="44" viewBox="0 0 47 44" aria-label="Menu" role="img">
      <g stroke="#3f5d7e" stroke-width="2.5"><line x1="0" y1="3" x2="47" y2="3"/><line x1="0" y1="15" x2="47" y2="15"/><line x1="0" y1="28" x2="47" y2="28"/><line x1="0" y1="41" x2="47" y2="41"/></g>
    </svg>
    <div class="app-name">Zorvy</div>
    <svg class="search-button" width="56" height="56" viewBox="0 0 56 56" aria-label="Search" role="img">
      <circle cx="36" cy="20" r="15" fill="none" stroke="#3f5d7e" stroke-width="2.5"/>
      <line x1="25" y1="31" x2="6" y2="50" stroke="#3f5d7e" stroke-width="7" stroke-linecap="round"/>
    </svg>
  </nav>

  <div class="feed-toggle">
    <span class="is-selected">all users</span>
    <span class="is-idle">following</span>
  </div>

  <section class="photo-stream">
    <div class="photo-card" style="left:117px; top:307px">
      <div class="photo-frame tone-blue" role="img" aria-label="Shared photo: final artwork">
        <span class="photo-tag">FA11 <svg width="11" height="10"><use href="#tag-heart"/></svg></span>
      </div>
      <p class="photo-name">Final Artwork</p><p class="photo-date">Created: 11/04/13</p>
    </div>
    <div class="photo-card" style="left:320px; top:307px">
      <div class="photo-frame tone-green" role="img" aria-label="Shared photo: drafts version 2">
        <span class="photo-tag">DV2 <svg width="11" height="10"><use href="#tag-heart"/></svg></span>
      </div>
      <p class="photo-name">Drafts Version 2</p><p class="photo-date">Created: 07/04/13</p>
    </div>
    <div class="photo-card" style="left:522px; top:307px">
      <div class="photo-frame tone-orange" role="img" aria-label="Shared photo: example images">
        <span class="photo-tag">EXI6 <svg width="11" height="10"><use href="#tag-heart"/></svg></span>
      </div>
      <p class="photo-name">Example Images</p><p class="photo-date">Created: 06/04/13</p>
    </div>
    <div class="photo-card" style="left:117px; top:561px">
      <div class="photo-frame tone-red" role="img" aria-label="Shared photo: edited text">
        <span class="photo-tag">TXE <svg width="11" height="10"><use href="#tag-heart"/></svg></span>
      </div>
      <p class="photo-name">Text (Edited)</p><p class="photo-date">Created: 06/04/13</p>
    </div>
    <div class="photo-card" style="left:320px; top:561px">
      <div class="photo-frame tone-yellow" role="img" aria-label="Shared photo: reference material">
        <span class="photo-tag">RFM <svg width="11" height="10"><use href="#tag-heart"/></svg></span>
      </div>
      <p class="photo-name">Reference Ma...</p><p class="photo-date">Created: 04/04/13</p>
    </div>
    <div class="photo-card" style="left:117px; top:789px">
      <div class="photo-frame tone-yellow" role="img" aria-label="Shared photo: reference image">
        <span class="photo-tag">RFI4 <svg width="11" height="10"><use href="#tag-heart"/></svg></span>
      </div>
      <p class="photo-name">Reference im...</p><p class="photo-date">Created: 04/04/13</p>
    </div>
    <div class="photo-card" style="left:320px; top:789px">
      <div class="photo-frame tone-green" role="img" aria-label="Shared photo: drafts version 1">
        <span class="photo-tag">DV1 <svg width="11" height="10"><use href="#tag-heart"/></svg></span>
      </div>
      <p class="photo-name">Drafts V1.</p><p class="photo-date">Created: 04/04/13</p>
    </div>
  </section>

  <footer class="dock">
    <div class="dock-item is-active" aria-current="page">
      <svg width="82" height="82" viewBox="0 0 82 82" role="img" aria-label="Feed, selected">
        <circle cx="41" cy="41" r="39" fill="none" stroke="currentColor" stroke-width="2"/>
        <path d="M41 62 C33 50 28 43 28 35 a13 13 0 0 1 26 0 c0 8 -5 15 -13 27 z" fill="currentColor"/>
        <circle cx="41" cy="35" r="4.5" fill="#7d7b48"/>
      </svg>
    </div>
    <div class="dock-item">
      <svg width="82" height="82" viewBox="0 0 82 82" role="img" aria-label="People">
        <circle cx="41" cy="41" r="39" fill="none" stroke="currentColor" stroke-width="2"/>
        <g fill="currentColor">
          <circle cx="26" cy="33" r="6"/><path d="M14 56 c0 -10 5 -15 12 -15 s12 5 12 15 z"/>
          <circle cx="56" cy="33" r="6"/><path d="M44 56 c0 -10 5 -15 12 -15 s12 5 12 15 z"/>
          <circle cx="41" cy="31" r="7.5" stroke="#c5d1b1" stroke-width="2"/><path d="M26 60 c0 -12 6 -19 15 -19 s15 7 15 19 z" stroke="#c5d1b1" stroke-width="2"/>
        </g>
      </svg>
    </div>
    <div class="dock-item">
      <svg width="82" height="82" viewBox="0 0 82 82" role="img" aria-label="Add photo">
        <circle cx="41" cy="41" r="39" fill="none" stroke="currentColor" stroke-width="2"/>
        <g stroke="currentColor" stroke-width="2.5"><line x1="41" y1="20" x2="41" y2="62"/><line x1="20" y1="41" x2="62" y2="41"/></g>
      </svg>
    </div>
    <div class="dock-item">
      <svg width="82" height="82" viewBox="0 0 82 82" role="img" aria-label="Activity, 3 new">
        <circle cx="41" cy="41" r="39" fill="none" stroke="currentColor" stroke-width="2"/>
        <path d="M41 58 C28 48 23 43 23 35 a9 9 0 0 1 18 -3 a9 9 0 0 1 18 3 c0 8 -5 13 -18 23 z" fill="currentColor"/>
      </svg>
      <span class="notice-badge">3</span>
    </div>
    <div class="dock-item">
      <svg width="82" height="82" viewBox="0 0 82 82" role="img" aria-label="Me">
        <circle cx="41" cy="41" r="39" fill="none" stroke="currentColor" stroke-width="2"/>
        <g fill="currentColor"><circle cx="42" cy="30" r="9"/><path d="M22 60 c0 -12 8 -19 20 -19 s20 7 20 19 z"/></g>
      </svg>
    </div>
  </footer>
</main>
</body>
</html>
```